Ridge Contracting LLC Business Card Design

I am looking for a creative and unique business card design. We are a commercial construction general contractor. With the name "RIDGE" Contracting, I am hoping to see some neat designs that correlate with the name.

```html
<!DOCTYPE html>
<html lang="en">
<head>
<meta charset="utf-8">
<title>Ridge Contracting LLC — Business Card</title>
<link rel="stylesheet" href="https://fonts.googleapis.com/css2?family=Arimo:wght@400;700&display=swap">
<style>
  :root {
    --backdrop: #5a5a5a;
    --card: #2d2d2d;
    --card-back: #2a2a2a;
    --accent: #2d9ad6;
    --text: #f2f2f2;
    --muted: #a8a8a8;
    --rule: #8a8a8a;
    --mark: #8c8c8c;
  }
  * { margin: 0; padding: 0; box-sizing: border-box; }
  html, body { width: 1200px; height: 1200px; overflow: hidden; }
  body {
    background: var(--backdrop);
    position: relative;
    font-family: "Arimo", Arial, sans-serif;
  }
  .card {
    position: absolute;
    width: 690px;
    height: 394px;
  }
  .card--front { left: 266px; top: 158px; background: var(--card); }
  .card--back  { left: 262px; top: 652px; background: var(--card-back); }

  .identity {
    position: absolute;
    right: 376px;
    top: 148px;
    text-align: right;
  }
  .identity__name {
    color: var(--accent);
    font-weight: 700;
    font-size: 26px;
    letter-spacing: 0.3px;
    line-height: 30px;
  }
  .identity__role {
    color: var(--muted);
    font-size: 15px;
    line-height: 22px;
  }
  .identity__address {
    color: var(--text);
    font-size: 16px;
    line-height: 20px;
    margin-top: 2px;
  }
  .divider {
    position: absolute;
    left: 330px;
    top: 154px;
    width: 1px;
    height: 82px;
    background: var(--rule);
  }
  .contacts {
    position: absolute;
    left: 353px;
    top: 153px;
    list-style: none;
  }
  .contacts__item {
    display: flex;
    align-items: center;
    height: 20.7px;
    color: var(--text);
    font-size: 16px;
  }
  .contacts__icon {
    width: 14px;
    height: 14px;
    margin-right: 9px;
    flex: none;
  }

  .brand {
    position: absolute;
    left: 0; right: 0;
    top: 170px;
    display: flex;
    align-items: center;
    justify-content: center;
    gap: 16px;
  }
  .brand__dot {
    width: 34px;
    height: 34px;
    border-radius: 50%;
    background: var(--mark);
  }
  .brand__name {
    color: var(--mark);
    font-weight: 700;
    font-size: 40px;
    letter-spacing: 4px;
  }
</style>
</head>
<body>
  <section class="card card--front" aria-label="Card front">
    <div class="identity">
      <p class="identity__name">DANIEL HART</p>
      <p class="identity__role">President</p>
      <p class="identity__address">412 Cedar Hollow Road<br>Halden, Canada 20418</p>
    </div>
    <div class="divider"></div>
    <ul class="contacts">
      <li class="contacts__item">
        <svg class="contacts__icon" viewBox="0 0 16 16"><path fill="var(--accent)" d="M3.2 1.5l2.4-.3 1.4 3.3-1.6 1.2c.8 1.8 2.1 3.1 3.9 3.9l1.2-1.6 3.3 1.4-.3 2.4c-.2 1.1-1.2 1.8-2.3 1.6C6.1 12.8 3.2 9.9 2.4 4.8c-.2-1.1.5-2.1 1.6-2.3z"/></svg>
        555-214-8830
      </li>
      <li class="contacts__item">
        <svg class="contacts__icon" viewBox="0 0 16 16"><rect x="4" y="1" width="8" height="14" rx="1.5" fill="none" stroke="var(--accent)" stroke-width="1.6"/><circle cx="8" cy="12.5" r=".9" fill="var(--accent)"/></svg>
        555-309-4172
      </li>
      <li class="contacts__item">
        <svg class="contacts__icon" viewBox="0 0 16 16"><rect x="1" y="3.5" width="14" height="10" fill="var(--accent)"/><path d="M1.5 4l6.5 5 6.5-5" fill="none" stroke="var(--card)" stroke-width="1.3"/></svg>
        info@ridgecontracting.com
      </li>
      <li class="contacts__item">
        <svg class="contacts__icon" viewBox="0 0 16 16"><circle cx="8" cy="8" r="7" fill="var(--accent)"/><path d="M5 4c1.5.5 2 2 1 3s-2 1-1.5 3M10 3.5c-1 1.5 0 2.5 1.5 2.5M9 13c0-2 2-2 2.5-3.5" fill="none" stroke="var(--card)" stroke-width="1.2"/></svg>
        www.ridgecontracting.com
      </li>
    </ul>
  </section>

  <section class="card card--back" aria-label="Card back">
    <div class="brand">
      <span class="brand__dot"></span>
      <span class="brand__name">RIDGE CONTRACTING</span>
    </div>
  </section>
</body>
</html>
```